Interfaith organization needs a poster advertising event for youth

We need a poster advertising our annual Lantern Gathering and Summit, where youth of all different religions come together for dialogue, friendship, fun, art, and musical performances. The poster should be have a front advertising the event, and the back should have more detailed descriptions of the event and submissions. It should be fun and eye catching!

Target Market(s)

Youth and Religious Organizations

Industry/Entity Type

Festival

Font styles to use
Serif

Requirements
Must have
• Pictures, poster-feel, contact information, etc. Logos of Bright Harbor Allies and Crossroads Young Leaders Circle of Maple Valley

```html
<!DOCTYPE html>
<html lang="en">
<head>
<meta charset="utf-8">
<title>Lantern Gathering and Summit Poster</title>
<link rel="stylesheet" href="https://fonts.googleapis.com/css2?family=Montserrat:ital,wght@0,400;0,600;0,700;0,800;1,800&family=Oswald:wght@300;400&family=Arimo:wght@400;700&display=swap">
<style>
  :root {
    --backdrop: #dcdcdc;
    --navy: #0f0c3e;
    --navy-deep: #080628;
    --ribbon-light: #5ea2e0;
    --ribbon-mid: #2f78c6;
    --ribbon-dark: #1b2468;
    --gold: #f5e51b;
    --orange: #f0a020;
    --title-yellow: #ffd21a;
    --white: #ffffff;
    --blue: #1a73c6;
    --ink: #333333;
    --ink-navy: #1d1a5c;
  }
  html, body {
    margin: 0;
    padding: 0;
    width: 1200px;
    height: 720px;
    overflow: hidden;
    background: var(--backdrop);
  }
  .canvas {
    position: relative;
    width: 1200px;
    height: 720px;
  }
  .poster {
    position: absolute;
    top: 20px;
    width: 490px;
    height: 680px;
    display: block;
  }
  .poster-front { left: 85px; }
  .poster-back { left: 625px; }
  .display { font-family: "Montserrat", sans-serif; }
  .thin { font-family: "Oswald", sans-serif; font-weight: 300; }
  .body { font-family: "Arimo", sans-serif; }
</style>
</head>
<body>
<main class="canvas">

  <!-- Front of poster -->
  <svg class="poster poster-front" viewBox="0 0 390 541" preserveAspectRatio="none" xmlns="http://www.w3.org/2000/svg">
    <defs>
      <linearGradient id="frontSky" x1="0" y1="0" x2="0" y2="1">
        <stop offset="0" stop-color="#1a1650"/>
        <stop offset="1" stop-color="#0a0830"/>
      </linearGradient>
      <linearGradient id="hallTone" x1="0" y1="0" x2="0" y2="1">
        <stop offset="0" stop-color="#9a9aa0"/>
        <stop offset="0.5" stop-color="#5e5a56"/>
        <stop offset="1" stop-color="#3a3436"/>
      </linearGradient>
    </defs>
    <rect class="front-bg" width="390" height="541" fill="url(#frontSky)"/>
    <rect class="hall-photo" x="0" y="0" width="390" height="200" fill="url(#hallTone)" role="img" aria-label="Photo of students seated at round tables in a large hall"/>

    <text class="display org-title" x="195" y="26" text-anchor="middle" font-size="14" font-weight="800" fill="var(--title-yellow)" textLength="340" lengthAdjust="spacingAndGlyphs">CROSSROADS YOUNG LEADERS CIRCLE</text>
    <text class="display org-subtitle" x="195" y="45" text-anchor="middle" font-size="13" font-weight="700" fill="var(--white)" letter-spacing="1">of Maple Valley's</text>

    <!-- ribbon -->
    <polygon class="ribbon-flap" points="0,180 60,168 62,212 0,222" fill="var(--ribbon-light)"/>
    <polygon class="ribbon-flap" points="300,150 390,122 390,250 330,205" fill="var(--ribbon-light)"/>
    <polygon class="ribbon-band" points="30,198 385,160 345,312 36,290" fill="var(--ribbon-mid)"/>
    <polygon class="ribbon-panel" points="40,218 345,182 320,300 40,288" fill="var(--ribbon-dark)"/>

    <circle class="org-badge" cx="90" cy="258" r="46" fill="var(--white)" stroke="var(--ribbon-mid)" stroke-width="3"/>
    <text class="display badge-name" x="90" y="250" text-anchor="middle" font-size="7" font-weight="700" fill="#b08a3a">
      <tspan x="90">Crossroads</tspan>
      <tspan x="90" dy="9">Young Leaders</tspan>
      <tspan x="90" dy="9">Circle</tspan>
    </text>

    <text class="thin edition-number" x="148" y="298" font-size="80" fill="var(--gold)">13</text>
    <text class="thin edition-label" font-size="16" fill="var(--white)">
      <tspan x="228" y="232">th</tspan>
      <tspan x="228" y="252">Annual</tspan>
      <tspan x="228" y="272" font-size="14">Lantern Gathering</tspan>
      <tspan x="228" y="292">&amp; Summit</tspan>
    </text>

    <text class="display tagline" x="195" y="360" text-anchor="middle" font-size="8.5" fill="var(--white)" letter-spacing="1">TEENS EXPRESSING THEIR</text>
    <text class="display tagline" x="195" y="375" text-anchor="middle" font-size="8.5" fill="var(--white)" letter-spacing="1">FAITH THROUGH ART, MUSIC, AND DIALOGUE</text>
    <text class="display event-kind" x="195" y="400" text-anchor="middle" font-size="11.5" font-weight="700" fill="var(--white)" letter-spacing="2">INTERFAITH YOUTH SUMMIT</text>
    <text class="display theme-label" x="195" y="430" text-anchor="middle" font-size="8.5" font-weight="700" fill="var(--white)" letter-spacing="1">THIS YEAR'S THEME</text>
    <text class="display theme" x="195" y="453" text-anchor="middle" font-size="17" font-weight="800" font-style="italic" fill="var(--gold)" letter-spacing="1">"Is Religion Cool?"</text>

    <text class="display date" x="195" y="487" text-anchor="middle" font-size="12.5" fill="var(--white)">19<tspan font-size="7" dy="-5">th</tspan><tspan dy="5"> March</tspan></text>
    <text class="display time" x="195" y="503" text-anchor="middle" font-size="7.5" fill="var(--orange)" letter-spacing="1">sunday ,2017 11:00am-5:00pm</text>
    <text class="display venue" x="195" y="518" text-anchor="middle" font-size="6.5" font-weight="700" fill="var(--white)">THE HARMONY HALL OF MAPLE VALLEY</text>
    <text class="display address" x="195" y="532" text-anchor="middle" font-size="7.5" fill="var(--orange)" letter-spacing="1">4150 Willowmere Ave, Maple Valley, CA 90000</text>
  </svg>

  <!-- Back of poster -->
  <svg class="poster poster-back" viewBox="0 0 366 508" preserveAspectRatio="none" xmlns="http://www.w3.org/2000/svg">
    <rect class="back-bg" width="366" height="508" fill="var(--white)"/>

    <text class="body intro" font-size="4.6" fill="var(--ink)">
      <tspan x="14" y="14">All high school age youth groups are invited to come and join with 150 to 175</tspan>
      <tspan x="14" y="20">other high school students from many faith traditions to take part in the</tspan>
      <tspan x="14" y="26">annual Lantern Summit. More than ever, our county and world need young</tspan>
      <tspan x="14" y="32">leaders who are willing to learn from each other and build stronger</tspan>
      <tspan x="14" y="38">communities together!</tspan>
    </text>

    <polygon class="section-bar" points="0,52 205,52 205,66 200,72 200,68 0,68" fill="var(--blue)"/>
    <text class="display section-title" x="9" y="63" font-size="7.5" font-weight="700" fill="var(--white)" letter-spacing="1.2">LANTERN SUMMIT</text>

    <text class="body summit-copy" font-size="4.6" fill="var(--ink)">
      <tspan x="9" y="84">The purpose of the Summit is to bring together young people from</tspan>
      <tspan x="9" y="90">diverse ethnic, cultural, and religious backgrounds, and to engage them in</tspan>
      <tspan x="9" y="96">dialogue. True dialogue is a conversation on a shared subject between two or</tspan>
      <tspan x="9" y="102">more people of differing points of view. We feel this commitment will affect</tspan>
      <tspan x="9" y="108">relationships in a constructive way in our places of worship and community.</tspan>
      <tspan x="9" y="114">Each table seats eight diverse high school students, one adult, and youth</tspan>
      <tspan x="9" y="120">leaders acting as facilitators, but it is stressed that it is the students</tspan>
      <tspan x="9" y="126">we want to hear from.</tspan>
      <tspan x="9" y="133" font-weight="700" fill="var(--ink-navy)">RSVP for our Lantern Summit by February 19th, 2017</tspan>
    </text>

    <polygon class="section-bar" points="0,146 205,146 205,160 200,166 200,162 0,162" fill="var(--blue)"/>
    <text class="display section-title" x="9" y="157" font-size="7.5" font-weight="700" fill="var(--white)" letter-spacing="1.2">LANTERN GATHERING</text>

    <text class="body gathering-copy" font-size="4.6" fill="var(--ink)">
      <tspan x="9" y="180">The summit will be followed by the Lantern Gathering where families of the</tspan>
      <tspan x="9" y="186">participants are welcome to join. The gathering will include musical</tspan>
      <tspan x="9" y="192">performances of all types from diverse religious communities, including but</tspan>
      <tspan x="9" y="198">not limited to singing, dancing, instrumental music and storytelling.</tspan>
      <tspan x="9" y="208" font-weight="700" fill="var(--ink-navy)">To take part in our Lantern Gathering (Music, Song, Dance), RSVP by</tspan>
      <tspan x="9" y="214" font-weight="700" fill="var(--ink-navy)">February 25th, 2017</tspan>
    </text>

    <!-- photo tiles -->
    <g class="photo-tile" transform="translate(300 62) rotate(-22)">
      <rect x="-52" y="-52" width="104" height="104" fill="var(--blue)"/>
      <rect x="-47" y="-47" width="94" height="94" fill="#c0463c" role="img" aria-label="Photo of a dancer in traditional costume performing"/>
    </g>
    <g class="photo-tile" transform="translate(258 132) rotate(-18)">
      <rect x="-42" y="-42" width="84" height="84" fill="var(--blue)"/>
      <rect x="-38" y="-38" width="76" height="76" fill="#8a7a72" role="img" aria-label="Photo of students seated in a circle talking"/>
    </g>
    <g class="photo-tile" transform="translate(318 190) rotate(12)">
      <rect x="-52" y="-52" width="104" height="104" fill="var(--blue)"/>
      <rect x="-47" y="-47" width="94" height="94" fill="#6f8aa0" role="img" aria-label="Photo of a flower arrangement beside a framed artwork"/>
    </g>
    <g class="photo-tile" transform="translate(120 330) rotate(-30)">
      <rect x="-78" y="-78" width="156" height="156" fill="var(--blue)"/>
      <rect x="-72" y="-72" width="144" height="144" fill="#b2a79a" role="img" aria-label="Photo of a drummer and a busy hall of students"/>
    </g>
    <g class="photo-tile" transform="translate(75 445) rotate(22)">
      <rect x="-62" y="-62" width="124" height="124" fill="var(--blue)"/>
      <rect x="-56" y="-56" width="112" height="112" fill="#c9a24a" role="img" aria-label="Photo of colorful student artwork on display tables"/>
    </g>

    <circle class="partner-mark" cx="335" cy="360" r="11" fill="none" stroke="var(--ink-navy)" stroke-width="1.6"/>
    <text class="display partner-name" font-size="12" font-weight="600" fill="var(--blue)">
      <tspan x="240" y="357">Bright Harbor</tspan>
      <tspan x="268" y="372">Allies</tspan>
    </text>

    <rect class="section-bar" x="185" y="420" width="181" height="15" fill="var(--blue)"/>
    <text class="display section-title" x="275" y="431" text-anchor="middle" font-size="7.5" font-weight="700" fill="var(--white)" letter-spacing="1.2">ART GALLERY</text>

    <text class="body gallery-copy" font-size="4.9" fill="var(--ink)">
      <tspan x="194" y="451">This event will include an Art Gallery display of stu-</tspan>
      <tspan x="194" y="459">dents' work, highlighting their expressions of faith, and</tspan>
      <tspan x="194" y="467">artwork promoting learning, understanding, leadership,</tspan>
      <tspan x="194" y="475">and service. Art includes any painting, illustration,</tspan>
      <tspan x="194" y="483">sculpture, photography or other visual art.</tspan>
      <tspan x="194" y="496" fill="var(--ink-navy)">Art Work for our Art Gallery must be submitted by: March</tspan>
    </text>
  </svg>

</main>
</body>
</html>
```